QTR tub packaging design

Hi!
We require a design for two different flavours of packaging for a protein recovery formula.
The design will be for the cardboard tubs as in pic attached. The name of the product will be 'LW recovery formula'. The LW logo is also attached and can be slightly adjusted.
The project will require a design for the front and then a basic design for the information on the back. This will include ingredients, nutrition info, directions and production location. On the back it will also need the 'lift your stride' logo and something referring to 'LW recovery formula by 'Your Vital Ember' (logo for this is attached).
The product will come in two flavours (cacao and coconut, then vanilla and acai) so will need the basic design adjusted for each flavour. The tubs are 1kg and this will need to be somewhere on the front of the tub.
This product is designed for healthy and active people, mainly female focused. The design should be clean and not overloaded with colours and pictures. It should only be two colours max. The final design should communicate that the product will assist people to reach their goals, whilst being health focused.

Target Market(s)

Active Females 20-50

Industry/Entity Type

Nutrition

Requirements
Must have
• Nutrition information and ingredients area
• Three logos attached
• Name- recovery formula
Should not have
• Not too busy, too many pictures or information. Please keep it simple.

```html
<!DOCTYPE html>
<html lang="en">
<head>
<meta charset="utf-8">
<title>LW Recovery Formula – Tub Front</title>
<link rel="stylesheet" href="https://fonts.googleapis.com/css2?family=Oswald:wght@400;500;600&family=Kaushan+Script&display=swap">
<style>
  :root {
    --backdrop: #e6e6e6;
    --kraft: #a58b69;
    --kraft-edge: #967c5b;
    --green: #7cc242;
    --ink: #333333;
    --label: #2b2b2b;
    --white: #ffffff;
  }
  * { margin: 0; padding: 0; box-sizing: border-box; }
  html, body { width: 1200px; height: 884px; overflow: hidden; }
  body { background: var(--backdrop); position: relative; font-family: "Oswald", sans-serif; }

  .tub-front {
    position: absolute; left: 300px; top: 112px; width: 608px; height: 748px;
    background: var(--kraft);
    border-radius: 6px;
  }
  .lid-seam {
    position: absolute; left: 0; right: 0; top: 244px; height: 2px;
    background: var(--kraft-edge);
  }

  .lid-mark {
    position: absolute; left: 0; right: 0; top: 8px;
    text-align: center;
  }
  .lid-mark .lid-name {
    color: var(--white); font-weight: 600; font-size: 34px; line-height: 36px; letter-spacing: 2px;
  }
  .lid-mark .lid-sub {
    color: var(--green); font-weight: 500; font-size: 9px; line-height: 10px; letter-spacing: 0.5px;
  }

  .flavour-label {
    position: absolute; left: 246px; top: 58px; width: 120px; height: 172px;
    background: var(--label);
    border-radius: 0 0 6px 6px;
    color: var(--green);
    text-align: center;
    padding-top: 12px;
    overflow: hidden;
  }
  .flavour-label .flavour-caption {
    font-family: "Kaushan Script", cursive;
    font-size: 22px; line-height: 28px;
  }
  .flavour-label .flavour-name {
    font-weight: 500; font-size: 28px; line-height: 38px; letter-spacing: -0.3px;
  }
  .flavour-label .flavour-join {
    display: flex; align-items: center; justify-content: center; gap: 5px;
    font-weight: 500; font-size: 22px; line-height: 30px;
  }
  .flavour-join::before, .flavour-join::after {
    content: ""; width: 16px; height: 6px;
    border-top: 2px solid var(--green); border-bottom: 2px solid var(--green);
  }

  .product-mark {
    position: absolute; left: 0; right: 0; top: 289px;
    text-align: center;
    color: var(--green);
    font-weight: 400; font-size: 228px; line-height: 228px; letter-spacing: 0;
  }
  .product-name {
    position: absolute; left: 213px; width: 202px; top: 542px;
    border-top: 2px solid var(--green); border-bottom: 2px solid var(--green);
    text-align: center; color: var(--ink);
    font-weight: 500; font-size: 24px; line-height: 30px; letter-spacing: 0.3px;
  }

  .maker {
    position: absolute; left: 0; right: 0; top: 598px;
    display: flex; flex-direction: column; align-items: center;
    color: var(--ink); font-weight: 500;
  }
  .maker-name { display: flex; align-items: center; gap: 8px; font-size: 50px; line-height: 56px; }
  .maker-dot { width: 16px; height: 16px; border-radius: 50%; background: var(--green); }
  .maker-sub { font-size: 14px; line-height: 18px; }
</style>
</head>
<body>
  <main class="tub-front">
    <div class="lid-mark">
      <div class="lid-name">LW</div>
      <div class="lid-sub">RECOVERY FORMULA</div>
    </div>

    <div class="lid-seam"></div>

    <div class="flavour-label">
      <div class="flavour-caption">flavour</div>
      <div class="flavour-name">CACAO</div>
      <div class="flavour-join">AND</div>
      <div class="flavour-name">COCONUT</div>
    </div>

    <div class="product-mark">LW</div>
    <div class="product-name">RECOVERY FORMULA</div>

    <div class="maker">
      <div class="maker-name">QTR<span class="maker-dot"></span></div>
      <div class="maker-sub">Your Vital Ember</div>
    </div>
  </main>
</body>
</html>
```